Black Friday Sale Social Media Graphics

Focusing on Black Friday Graphics for each of the pics attached.  So need the product pics turned into  social media graphics (square size). For the color scheme of the graphics, they should all be complementary to the product colors.
You can add any of the stock photography attached but none are required. I mainly need BOLD text that says:
Black Friday Sale
Up to $15 Off
If you wanted to add smaller text, these headlines can work:
1.	Burn Belly Fat Fast!
2.	Double Your Weight Loss With Our Supplements!
3.	Lose Weight Naturally: Ditch the Prescription Pills & Needles!
4.	Tired of Stubborn Belly Fat? Discover What Works!
5.	Melt Away Belly Fat Faster with Our Supplements!
6.	Struggling to Lose Weight? Discover the Ultimate Solution!
7.	Ready to Burn Fat Faster?

Target Market(s)
women trying to lose weight
Industry/Entity Type
health and wellness
Requirements
Must have
- the product pics attached

Nice to have
- Bold text that says: Black Friday Sale

```html
<!DOCTYPE html>
<html lang="en">
<head>
<meta charset="utf-8">
<title>Black Friday Sale</title>
<link rel="stylesheet" href="https://fonts.googleapis.com/css2?family=Fira+Sans:wght@800;900&family=Roboto+Condensed:wght@700&display=swap">
<style>
  :root {
    --bg-dark: #3b393a;
    --floor-top: #707072;
    --floor-bottom: #3f3e40;
    --white: #ffffff;
    --ink: #2e2c2d;
    --yellow: #fbea16;
    --rose: #cf5f70;
    --teal: #3d6b72;
    --indigo: #4b4aa9;
    --orchid: #c27cc2;
    --band: #c880c7;
  }
  * { margin: 0; padding: 0; box-sizing: border-box; }
  html, body { width: 1200px; height: 1200px; overflow: hidden; background: var(--bg-dark); }
  .canvas {
    position: relative;
    width: 1200px;
    height: 1200px;
    overflow: hidden;
    background: var(--bg-dark);
    font-family: "Fira Sans", sans-serif;
  }
  .floor {
    position: absolute;
    left: 0; top: 881px;
    width: 1200px; height: 319px;
    background: linear-gradient(to bottom, var(--floor-top), var(--floor-bottom));
  }
  .accent-band {
    position: absolute;
    left: 0; top: 0;
    width: 1200px; height: 1200px;
  }
  .headline {
    position: absolute;
    left: 40px; top: 40px;
    width: 530px;
    text-align: center;
    color: var(--white);
    font-weight: 900;
    font-size: 176px;
    line-height: 163px;
    letter-spacing: -4px;
  }
  .offer-badge {
    position: absolute;
    left: 115px; top: 566px;
    width: 374px; height: 374px;
    border-radius: 50%;
    background: var(--yellow);
    color: var(--ink);
    text-align: center;
    font-weight: 900;
  }
  .offer-badge .lead { position: absolute; left: 0; right: 0; top: 22px; font-size: 70px; line-height: 1; letter-spacing: -2px; }
  .offer-badge .amount { position: absolute; left: 0; right: 0; top: 88px; font-size: 178px; line-height: 1; letter-spacing: -8px; }
  .offer-badge .tail { position: absolute; left: 0; right: 0; top: 262px; font-size: 86px; line-height: 1; letter-spacing: -2px; }
  .hero-photo {
    position: absolute;
    left: 520px; top: 55px;
    width: 632px; height: 902px;
    background: radial-gradient(ellipse at 55% 45%, #e9e6e6 0%, #b89584 35%, #5a4a48 70%, rgba(59,57,58,0) 100%);
  }
  .tag {
    position: absolute;
    padding: 2px 8px 3px;
    font-family: "Roboto Condensed", sans-serif;
    font-weight: 700;
    font-size: 22px;
    line-height: 28px;
    color: var(--white);
    white-space: nowrap;
    transform: rotate(-2deg);
    transform-origin: left center;
  }
  .tag-rose { background: var(--rose); }
  .tag-teal { background: var(--teal); }
  .tag-indigo { background: var(--indigo); }
  .tag-orchid { background: var(--orchid); }
</style>
</head>
<body>
<main class="canvas">
  <div class="floor"></div>
  <svg class="accent-band" viewBox="0 0 1200 1200" aria-hidden="true">
    <polygon points="0,1200 0,1188 1200,1146 1200,1200" fill="var(--band)"/>
  </svg>

  <div class="hero-photo" role="img" aria-label="Smiling woman in a white cropped sweater pointing at her waist, with a row of cream tubes and supplement bottles on the table in front of her"></div>

  <h1 class="headline">Black<br>Friday<br>Sale</h1>

  <div class="offer-badge">
    <span class="lead">up to</span>
    <span class="amount">$15</span>
    <span class="tail">Off</span>
  </div>

  <p class="tag tag-rose" style="left:62px;top:962px;">Burn Belly Fat Fast!</p>
  <p class="tag tag-teal" style="left:66px;top:1006px;">Lose Weight Naturally: Ditch the Prescription Pills &amp; Needles!</p>
  <p class="tag tag-indigo" style="left:670px;top:988px;">Ready to Burn Fat Faster?</p>
  <p class="tag tag-orchid" style="left:66px;top:1062px;">Double Your Weight Loss With Our Supplements!</p>
  <p class="tag tag-rose" style="left:556px;top:1040px;">Melt Away Belly Fat Faster with Our Supplements!</p>
  <p class="tag tag-teal" style="left:69px;top:1118px;">Tired of Stubborn Belly Fat? Discover What Works!</p>
  <p class="tag tag-teal" style="left:570px;top:1096px;">Struggling to Lose Weight? Discover the Ultimate Solution!</p>
</main>
</body>
</html>
```